Business cards, envelopes and letterhead
Simple but professional
Business cards, envelopes and letterhead -
Creative Brief
Professional
Martin Doyle
President & CEO
4273 Beldon Street Chilliwack, BC V4K 7N2 Canada
mdoyle@fernobrix.com
www.fernobrix.com
On the back, we want at least the logo (maybe the styled water drop only, we might not need the "FERNOBRIX" there but that's up to the designer), and we want to have a lot of white space so people can make notes on this when decided (though we don't need lines on the back for writing or so).

```html
<!DOCTYPE html>
<html lang="en">
<head>
<meta charset="utf-8">
<title>Fernobrix Letterhead</title>
<link rel="stylesheet" href="https://fonts.googleapis.com/css2?family=Exo+2:wght@700&family=PT+Serif&display=swap">
<style>
  :root {
    --canvas-bg: #ffffff;
    --paper: #ffffff;
    --paper-edge: #2a2a2a;
    --brand-navy: #1b4f93;
    --accent-light: #7fd0f0;
    --accent-mid: #3fb4e6;
    --text-grey: #8a8a8a;
    --band-text: #ffffff;
  }
  html, body {
    margin: 0;
    padding: 0;
    width: 1200px;
    height: 871px;
    overflow: hidden;
    background: var(--canvas-bg);
  }
  .canvas {
    position: relative;
    width: 1200px;
    height: 871px;
  }
  .letterhead {
    position: absolute;
    left: 312px;
    top: 36px;
    width: 632px;
    height: 830px;
    background: var(--paper);
    border: 1.5px solid var(--paper-edge);
    box-shadow: 2px 3px 6px rgba(0,0,0,0.25);
    box-sizing: border-box;
    overflow: hidden;
  }
  .brand {
    position: absolute;
    left: 96px;
    top: 88px;
    display: flex;
    align-items: center;
    gap: 8px;
  }
  .brand-dot {
    width: 14px;
    height: 14px;
    border-radius: 50%;
    background: var(--brand-navy);
  }
  .brand-name {
    font-family: "Exo 2", Arial, sans-serif;
    font-weight: 700;
    font-size: 33px;
    letter-spacing: 0.5px;
    color: var(--brand-navy);
    line-height: 1;
  }
  .address {
    position: absolute;
    left: 118px;
    top: 126px;
    font-family: "PT Serif", Georgia, serif;
    font-size: 8.5px;
    line-height: 14px;
    color: var(--text-grey);
  }
  .corner-accent {
    position: absolute;
    right: 0;
    bottom: 24px;
    width: 150px;
    height: 120px;
    background: linear-gradient(135deg, rgba(127,208,240,0) 40%, rgba(127,208,240,0.55) 100%);
  }
  .footer-band {
    position: absolute;
    left: 0;
    right: 0;
    bottom: 0;
    height: 24px;
    background: var(--brand-navy);
  }
  .footer-web {
    position: absolute;
    left: 110px;
    bottom: 6px;
    font-family: "PT Serif", Georgia, serif;
    font-size: 10px;
    letter-spacing: 3px;
    color: var(--band-text);
  }
</style>
</head>
<body>
<div class="canvas">
  <div class="letterhead">
    <div class="brand">
      <span class="brand-dot"></span>
      <span class="brand-name">FERNOBRIX</span>
    </div>
    <div class="address">
      4273 Beldon Street Chilliwack, BC<br>
      V4K 7N2 Canada | mdoyle@fernobrix.com
    </div>
    <div class="corner-accent" role="img" aria-label="Decorative light blue accent area in the lower right corner"></div>
    <div class="footer-band"></div>
    <div class="footer-web">www.fernobrix.com</div>
  </div>
</div>
</body>
</html>
```